Namecard design for Forex trading & training company

We need a design for a financial forex trading company.
Namecard should give customer a professional yet premium feel, able to differentiate from others.
1) most financial companies employs white background, while its clean and professional, it is too mainstream.
2) I am thinking of brown as base colour, however it easily gives the perception of being an Interior Design company
3) Task is to find a design that is able to portray a clean professional feel, at the same time, appear premium and differentiated from others.
*I'll be employing 3D textured print for my company namecard just so as to give it a better finishing.
Please find attached for my logo.
Financial

```html
<!DOCTYPE html>
<html lang="en">
<head>
<meta charset="utf-8">
<title>Veltra Capital – Business Card</title>
<link href="https://fonts.googleapis.com/css2?family=Cinzel:wght@400&family=Lato:wght@300;400&display=swap" rel="stylesheet">
<style>
  :root {
    --backdrop: #1b1b1c;
    --card: #3a3a3c;
    --card-edge: #444446;
    --ink: #d9d9d9;
    --ink-soft: #b5b5b7;
    --accent: #5ab3d6;
  }
  * { box-sizing: border-box; margin: 0; padding: 0; }
  html, body {
    width: 1200px; height: 997px; overflow: hidden;
    background: var(--backdrop);
  }
  .canvas {
    width: 1200px; height: 997px;
    display: flex; flex-direction: column; align-items: center; justify-content: center;
    gap: 60px;
  }
  .card {
    width: 700px; height: 400px;
    background: var(--card);
    border: 1px solid var(--card-edge);
    box-shadow: 0 18px 40px rgba(0,0,0,.55);
    position: relative;
  }
  .brand-name {
    font-family: "Cinzel", serif;
    font-weight: 400;
    color: var(--ink);
    letter-spacing: .22em;
    display: flex; align-items: center; gap: 14px;
    white-space: nowrap;
  }
  .brand-name .mark {
    width: 14px; height: 14px; background: var(--ink); flex: none;
  }

  /* front */
  .card--front {
    display: flex; flex-direction: column; align-items: center; justify-content: center;
  }
  .card--front .brand-name { font-size: 30px; }
  .rule {
    width: 260px; height: 1px; margin: 28px 0 22px;
    background: linear-gradient(90deg, transparent, var(--ink-soft), transparent);
  }
  .website {
    font-family: "Lato", sans-serif; font-size: 19px; color: var(--accent); letter-spacing: .02em;
  }

  /* back */
  .card--back { display: flex; align-items: center; }
  .card--back .brand-panel {
    width: 330px; display: flex; justify-content: center;
  }
  .card--back .brand-name { font-size: 24px; }
  .divider {
    width: 2px; height: 180px;
    background: linear-gradient(180deg, transparent, var(--ink), transparent);
  }
  .details { padding-left: 36px; font-family: "Lato", sans-serif; }
  .person-name { font-size: 24px; font-weight: 400; color: var(--ink); letter-spacing: .03em; }
  .person-role { font-size: 17px; font-weight: 400; color: var(--accent); margin-top: 2px; }
  .contact-list { list-style: none; margin-top: 34px; }
  .contact-list li {
    display: flex; align-items: center; gap: 14px;
    font-size: 15px; font-weight: 300; color: var(--ink); letter-spacing: .03em;
    margin-bottom: 12px;
  }
  .contact-list svg { width: 14px; height: 14px; flex: none; }
</style>
</head>
<body>
<main class="canvas">
  <section class="card card--front">
    <div class="brand-name"><span class="mark"></span>Veltra Capital</div>
    <div class="rule"></div>
    <div class="website">www.veltracap.com</div>
  </section>

  <section class="card card--back">
    <div class="brand-panel">
      <div class="brand-name"><span class="mark"></span>Veltra Capital</div>
    </div>
    <div class="divider"></div>
    <div class="details">
      <h1 class="person-name">DANIEL HALE</h1>
      <p class="person-role">Chief Executive Officer</p>
      <ul class="contact-list">
        <li>
          <svg viewBox="0 0 14 14"><rect x="3" y="1" width="8" height="12" rx="1.5" fill="none" stroke="var(--accent)" stroke-width="1.4"/></svg>
          +852 6100 4420
        </li>
        <li>
          <svg viewBox="0 0 14 14"><rect x="1" y="3" width="12" height="8" fill="var(--accent)"/><path d="M1 3l6 5 6-5" fill="none" stroke="var(--card)" stroke-width="1.2"/></svg>
          enquiries@veltracap.com
        </li>
        <li>
          <svg viewBox="0 0 14 14"><path d="M7 1a4 4 0 0 1 4 4c0 3-4 8-4 8S3 8 3 5a4 4 0 0 1 4-4z" fill="var(--accent)"/><circle cx="7" cy="5" r="1.4" fill="var(--card)"/></svg>
          Harbor Plaza F12-16, Bay Island
        </li>
      </ul>
    </div>
  </section>
</main>
</body>
</html>
```